Book a Belle needs a Stunning web design

Book a Belle is an upmarket agency in Sydney that has lingerie waitresses for events.

Book a Belle is looking for a website design that is as sexy and sophisticated as the ladies who work for them!

The design mustn't be cluttered, tacky or pornographic. What I'm looking for is something better than the industry leader www.velvetgrace.com.au Something classy, sexy and different.

When designing please suggest a CMS, we already use wordpress but are open to suggestions.

We will need a home page that incorporates a feed from a blog and/or social media (please make suggestions and use your discretion as a designer, however we'd like to approve what goes into the feed before it goes in.) The home page could also have a list of our services, but if not we will need a services page. Our Services include:
Lingerie waitressing at events
Lingerie waitresses to help dress the groom pre wedding.
Bucks parties

We have a logo that we'd like incorporated into the design and have attached it.

We will also need a portfolio page for the ladies, This is not to be cluttered, tacky or pornographic. It needs to be classy.

We will also need a "Contact us" page and were thinking that this could potentially also be a "Ask for a quote on your event" page. I.e. have a regular "Contact us" form but have alternate fields if they tick the "I want a quote" box. Alternatively you could have two parts to the contact us page. One that is a regular form and one that has a "Your requirements" box.

Again please use your discretion when designing these, if it's too cluttered it won't work. If it looks tacky, don't do it. If you have suggestions make them.

Target Market(s)

Males between the ages of 18 - 45

Industry/Entity Type

Industry

Requirements
Must have
• Must incorporate our logo.

```html
<!DOCTYPE html>
<html lang="en">
<head>
<meta charset="utf-8">
<title>Book a Belle – Web Design</title>
<link rel="stylesheet" href="https://fonts.googleapis.com/css2?family=PT+Serif&family=Lobster&family=Questrial&display=swap">
<style>
  :root {
    --stage: #ececec;
    --stage-light: #f8f8f8;
    --ink: #111111;
    --magenta: #c814a8;
    --magenta-bright: #e63fd2;
    --magenta-soft: #f05ce0;
    --purple: #8a1aa6;
    --purple-deep: #5e0f78;
    --screen: #1b1b1b;
    --lace: #d6d6d6;
    --lace-light: #e6e6e6;
    --white: #ffffff;
    --plum: #3a1838;
  }
  * { box-sizing: border-box; margin: 0; padding: 0; }
  html, body { width: 1200px; height: 848px; overflow: hidden; }
  body {
    position: relative;
    background: radial-gradient(ellipse at 50% 45%, var(--stage-light), var(--stage) 70%);
    font-family: "PT Serif", serif;
  }
  .corner-stripe {
    position: absolute; left: -40px; top: 20px;
    width: 320px; height: 34px; background: var(--ink);
    transform: rotate(-25deg); transform-origin: left top;
  }
  .page {
    position: absolute; left: 272px; top: 51px;
    width: 657px; height: 664px;
    background: var(--white);
    box-shadow: 0 4px 12px rgba(0,0,0,.35);
    overflow: hidden;
  }
  .lace {
    position: absolute; top: 120px; width: 80px; height: 500px;
    background:
      linear-gradient(to right, rgba(255,255,255,0), var(--lace) 25%, var(--lace-light) 50%, var(--lace) 75%, rgba(255,255,255,0));
  }
  .lace--left { left: 28px; }
  .lace--right { left: 564px; }
  .page-sides { position: absolute; inset: 0; }
  .content {
    position: absolute; left: 107px; top: 0; width: 458px; height: 664px;
    background: radial-gradient(ellipse at 50% 40%, var(--magenta-bright), var(--magenta) 70%);
  }
  .brand {
    position: absolute; left: 0; width: 100%; top: 108px;
    text-align: center; font-size: 40px; font-weight: 400; color: var(--ink);
  }
  .chandelier {
    position: absolute; left: 85px; top: 190px; width: 290px; height: 90px;
    background: radial-gradient(ellipse at 50% 30%, rgba(255,255,255,.35), rgba(255,255,255,0) 70%);
  }
  .main-nav {
    position: absolute; left: 0; top: 303px; width: 100%; height: 38px;
    background: linear-gradient(var(--magenta-soft), var(--magenta));
    border-top: 1px solid rgba(255,255,255,.35);
    border-bottom: 1px solid rgba(255,255,255,.35);
  }
  .nav-item {
    position: absolute; top: 0; height: 38px; line-height: 38px;
    text-align: center; font-size: 13px; color: var(--white);
    border-right: 1px solid rgba(255,255,255,.25);
  }
  .nav-item--muted { color: var(--purple-deep); }
  .nav-item--active {
    height: 46px;
    background: linear-gradient(var(--purple), var(--purple-deep));
    box-shadow: 0 3px 6px rgba(0,0,0,.35);
    border: none;
  }
  .dropdown { position: absolute; left: 211px; top: 351px; width: 144px; list-style: none; }
  .dropdown-item {
    height: 36px; margin-bottom: 2px; line-height: 36px;
    text-align: center; font-size: 11.5px; color: var(--white);
    background: linear-gradient(var(--purple), var(--purple-deep) 80%);
    box-shadow: 0 2px 4px rgba(0,0,0,.3);
  }
  .video {
    position: absolute; left: 15px; width: 176px; height: 119px;
    background: var(--magenta-soft); padding: 6px;
    box-shadow: 0 8px 10px -6px rgba(0,0,0,.45);
  }
  .video--one { top: 377px; }
  .video--two { top: 519px; }
  .video-screen { position: relative; width: 100%; height: 100%; background: var(--screen); }
  .video-dots { position: absolute; left: 4px; bottom: 4px; display: flex; gap: 2px; }
  .video-dots span { width: 7px; height: 7px; border-radius: 50%; background: var(--magenta); }
  .video-dots span + span { background: var(--purple); }
  .quote-badge { position: absolute; left: 243px; top: 485px; width: 176px; height: 146px; }
  .quote-badge p {
    position: absolute; inset: 0; display: flex; align-items: center; justify-content: center;
    text-align: center; font-family: "Lobster", cursive; font-size: 30px; line-height: 1;
    color: var(--white);
  }
  .caption-bar {
    position: absolute; left: 0; top: 793px; width: 1200px; height: 55px;
    background: var(--ink); color: var(--white);
    font-family: "Questrial", sans-serif; font-size: 15px;
    padding: 18px 0 0 62px;
  }
</style>
</head>
<body>
  <div class="corner-stripe"></div>

  <main class="page">
    <div class="lace lace--left" role="img" aria-label="White lace trim pattern"></div>
    <div class="lace lace--right" role="img" aria-label="White lace trim pattern"></div>
    <svg class="page-sides" width="657" height="664" viewBox="0 0 657 664">
      <path d="M0 0 H107 V48 Q40 55 0 85 Z" fill="#111"/>
      <path d="M0 664 V626 Q50 575 107 555 V664 Z" fill="#111"/>
      <path d="M565 0 H657 V165 Q615 140 565 128 Z" fill="#111"/>
      <path d="M565 664 V610 Q615 560 657 555 V664 Z" fill="#111"/>
    </svg>

    <section class="content">
      <h1 class="brand">Book a Belle</h1>
      <div class="chandelier" role="img" aria-label="Strings of white pearls hanging below the logo with a tassel"></div>

      <nav class="main-nav">
        <span class="nav-item" style="left:0;width:92px">HOME</span>
        <span class="nav-item nav-item--muted" style="left:92px;width:117px">SERVICES</span>
        <span class="nav-item nav-item--active" style="left:211px;width:144px">PORTFOLIO</span>
        <span class="nav-item nav-item--muted" style="left:357px;width:101px;border-right:none">CONTACT</span>
      </nav>

      <ul class="dropdown">
        <li class="dropdown-item">BELLE NAME</li>
        <li class="dropdown-item">BELLE NAME</li>
        <li class="dropdown-item">BELLE NAME</li>
      </ul>

      <div class="video video--one"><div class="video-screen"><div class="video-dots"><span></span><span></span></div></div></div>
      <div class="video video--two"><div class="video-screen"><div class="video-dots"><span></span><span></span></div></div></div>

      <div class="quote-badge">
        <svg width="176" height="146" viewBox="0 0 176 146">
          <path d="M88 4 Q120 4 140 18 Q172 30 172 73 Q172 116 140 128 Q120 142 88 142 Q56 142 36 128 Q4 116 4 73 Q4 30 36 18 Q56 4 88 4 Z" fill="#111"/>
          <path d="M88 16 Q116 16 134 28 Q160 38 160 73 Q160 108 134 118 Q116 130 88 130 Q60 130 42 118 Q16 108 16 73 Q16 38 42 28 Q60 16 88 16 Z" fill="#3a1838" stroke="#888" stroke-width="1.5"/>
        </svg>
        <p>I want<br>a quote</p>
      </div>
    </section>
  </main>

  <footer class="caption-bar">Book a Belle needs a Stunning web design</footer>
</body>
</html>
```